Bar and Grill looking or a Responsive Web design

New Bar and Grill in the Toronto area just opened up and is looking for a new wordpress website to start off his business.

Their business revolves around a homey family, upbeat atmosphere. His cuisine is gourmet pub style food. Speciality are home made burgers. 90 Seat restaurant in a very diverse and high density neighbourhood.

Looking for a responsive web design that will focus on a key feature pages.

Homepage
- Navigation is easy and simple, emphasize easy navigation in Mobile view.
- Contact information is a click or touch away

About Page

Menu Page
-Menu styling to be responsive. Very simple navigation through different menus and then menu would appear.

Gallery

Contact page
- Map (not googlesk)
- Contact Details
- Contact/Feedback form

They do have a logo and will be uploaded.

We are open to any designs, as well as designs based off templates that have already been created.

Target Market(s)

Target audience is the varied. They are in an area that's densely populated and very diverse. Looking for a crowd that appreciates a setting for sports, good gourmet pub styled food and a home styled restaurant.

Industry/Entity Type

Restaurant

Colors

Designer to choose colors to be used in the design.

Requirements
Must have
• Menus have to have responsive design for both mobile and tablet/desktop.
Nice to have
• Easy access contact button on mobile view. That way it will act like a webapp so that mobile devices can take advantage of quick touches to get in contact.

```html
<!DOCTYPE html>
<html lang="en">
<head>
<meta charset="utf-8">
<title>Oakbarrel — Bar &amp; Grill</title>
<link href="https://fonts.googleapis.com/css2?family=Ubuntu:ital,wght@0,400;0,500;0,700;1,400;1,700&display=swap" rel="stylesheet">
<style>
:root{
  --green:#6aa92e;
  --green-dark:#4f8a26;
  --green-deep:#3e6d1d;
  --red:#e8231c;
  --ink:#1e1e1e;
  --text:#3a3a3a;
  --page:#f2f4f0;
  --field:#dcdedb;
  --white:#ffffff;
}
*{margin:0;padding:0;box-sizing:border-box}
html,body{width:982px;height:1200px;overflow:hidden}
body{font-family:'Ubuntu',sans-serif;background:var(--page);color:var(--text);position:relative}
.abs{position:absolute}
.topbar{left:0;top:0;width:982px;height:20px;background:var(--green);color:var(--white);font-size:7.5px;line-height:20px}
.topbar .msg{left:183px;top:0}
.topbar .msg b{font-weight:700}
.topbar .msg i{font-style:italic;font-weight:700}
.topbar .social{right:182px;top:5px;display:flex;gap:4px}
.topbar .social span{width:10px;height:10px;background:var(--white);border-radius:1px;display:block}
.header{left:0;top:20px;width:982px;height:81px;background:var(--white)}
.brand{left:186px;top:42px;font-size:24px;font-weight:500;color:var(--red);letter-spacing:.5px}
.nav a{position:absolute;top:57px;font-size:9.5px;color:var(--green-dark);text-decoration:none;text-transform:uppercase}
.nav a.active{color:var(--red);font-weight:700;border-bottom:2px solid var(--red);padding:0 3px 5px}
.hero{left:0;top:101px;width:982px;height:289px;
  background:radial-gradient(ellipse at 45% 40%,#d8432a 0%,#a53a2c 30%,transparent 60%),
  radial-gradient(ellipse at 78% 62%,#3e8a1d 0%,transparent 22%),
  linear-gradient(180deg,#c9c7c0 0%,#8a4a3a 40%,#5a2a20 75%,#d9d6d0 100%)}
.rule{height:0;border-top:2px dotted #7db64a}
.h2{font-size:12px;font-weight:500;color:var(--ink);text-transform:uppercase}
.h2 em{font-style:normal;color:var(--red);font-weight:700}
.photo{border:2px solid var(--white)}
.body{font-size:7.5px;line-height:9.5px;color:var(--text)}
.btn{background:var(--green-dark);color:var(--white);font-size:7.5px;font-weight:700;text-transform:uppercase;display:flex;align-items:center;justify-content:center}
.svc{display:flex;align-items:center;font-size:7.5px}
.svc i{width:26px;height:9px;border:1px solid var(--red);border-radius:2px;margin-right:18px;display:block}
.viewall{font-size:6px;color:var(--green-dark);font-weight:500}
.arrows{display:flex;gap:5px}
.arrows span{width:11px;height:11px;background:var(--red);display:flex;align-items:center;justify-content:center}
.dish{width:142px}
.dish .img{width:142px;height:87px}
.dish h3{font-size:8.5px;font-weight:700;color:var(--ink);margin-top:19px}
.dish p{font-size:7.5px;line-height:9.5px;margin-top:3px}
.dish .row{display:flex;justify-content:space-between;margin-top:11px}
.dish .row .btn{height:18px}
.quote{font-size:7.5px;line-height:9.5px}
.quote b{display:block;font-style:italic;font-weight:700;color:var(--ink)}
.field{background:var(--field);color:#8a8a8a;font-size:7px;font-style:italic;text-transform:uppercase;padding-left:8px;display:flex;align-items:center;justify-content:space-between;padding-right:8px}
.icons{display:flex;gap:9px}
.icons span{width:14px;height:14px;border-radius:2px;display:block}
.footer{left:0;top:1139px;width:982px;height:41px;background:var(--green-dark)}
.footer a{position:absolute;top:22px;transform:translateY(-50%);font-size:9.5px;color:var(--white);text-decoration:none;text-transform:uppercase}
.footer a.active{font-weight:700}
.footer .brand-f{right:196px;top:11px;font-size:16px;font-weight:500;color:var(--white)}
.legal{left:0;top:1180px;width:982px;height:20px;background:var(--green-deep);color:#e5eedb;font-size:6px;line-height:20px;text-align:center}
</style>
</head>
<body>
<div class="abs topbar">
  <div class="abs msg">Welcome to <b>oakbarrel</b>, learn more about us,our recipies, special dishes &amp; the <i>taste</i> which you can never forget.</div>
  <div class="abs social" aria-label="Social links"><span></span><span></span><span></span><span></span><span></span></div>
</div>

<header class="abs header">
  <div class="abs brand" style="top:22px">OAKBARREL</div>
  <nav class="nav">
    <a class="active" style="left:403px;top:37px">Home</a>
    <a style="left:454px;top:37px">Menu</a>
    <a style="left:502px;top:37px">Recepies</a>
    <a style="left:563px;top:37px">Portfolio</a>
    <a style="left:634px;top:37px">News</a>
    <a style="left:681px;top:37px">About Us</a>
    <a style="left:744px;top:37px">Contact Us</a>
  </nav>
</header>

<div class="abs hero" role="img" aria-label="Close-up of sliced grilled steak topped with tomato and onion salsa, with broccoli and roast potatoes"></div>

<!-- Welcome -->
<div class="abs rule" style="left:183px;top:416px;width:300px"></div>
<div class="abs rule" style="left:501px;top:416px;width:299px"></div>
<div class="abs h2" style="left:182px;top:437px">Welcome to <em>Oakbarrel</em></div>
<div class="abs photo" role="img" aria-label="Warm-lit restaurant dining room with pendant lamps and set tables" style="left:183px;top:469px;width:115px;height:97px;background:linear-gradient(160deg,#c98a2e,#5a2018 55%,#2a1410)"></div>
<p class="abs body" style="left:311px;top:471px;width:174px">This is Photoshop's version &nbsp;of Lorem Ipsum. Proin gravida nibh vel velit auctor aliquet. Aenean sollicitudin, lorem quis bibendum auctor, nisi elit consequat ipsum, nec sagittis sem nibh id elit.<br>Duis sed odio sit amet nibh vulputate cursus a sit amet mauris. Morbi accumsan ipsum velit.</p>
<div class="abs btn" style="left:311px;top:550px;width:80px;height:17px">View More</div>

<div class="abs h2" style="left:498px;top:437px">Featured <em>Services</em></div>
<div class="abs" style="left:505px;top:470px;display:flex;flex-direction:column;gap:10px">
  <div class="svc"><i></i>90 Seat restaurant in a very diverse and high density neighbourhood.</div>
  <div class="svc"><i></i>Tasty food with better hospitality.</div>
  <div class="svc"><i></i>Celebrate your Birthdays and Annversary party</div>
  <div class="svc"><i></i>Home delivery &amp; Gift vouchers avalible.</div>
</div>
<div class="abs btn" style="left:628px;top:550px;width:80px;height:17px">View More</div>
<div class="abs rule" style="left:183px;top:585px;width:300px"></div>
<div class="abs rule" style="left:501px;top:585px;width:299px"></div>

<!-- Dishes -->
<div class="abs h2" style="left:185px;top:612px">Our <em>Dishes</em></div>
<div class="abs viewall" style="left:770px;top:603px">VIEW ALL</div>
<div class="abs arrows" style="left:770px;top:617px">
  <span><svg width="5" height="6" viewBox="0 0 5 6"><path d="M4 0L0 3l4 3z" fill="#fff"/></svg></span>
  <span><svg width="5" height="6" viewBox="0 0 5 6"><path d="M1 0l4 3-4 3z" fill="#fff"/></svg></span>
</div>

<div class="abs dish" style="left:184px;top:646px">
  <div class="img photo" role="img" aria-label="Fried cutlet with sauce, corn and fries" style="background:linear-gradient(150deg,#c7d58a,#b86a22 45%,#f0c42a)"></div>
  <h3>PROIN GRAVIDA</h3>
  <p>Nibh vel velit auctor aliquet. Aenean sollicitudin, lorem quis bibendum.</p>
  <div class="row"><div class="btn" style="width:77px">Learn More</div><div class="btn" style="width:37px">$ 25</div></div>
</div>
<div class="abs dish" style="left:341px;top:646px">
  <div class="img photo" role="img" aria-label="Grilled patties with dip and corn salad" style="background:linear-gradient(150deg,#9a8e80,#4a3324 50%,#6a4a2a)"></div>
  <h3>PROIN GRAVIDA</h3>
  <p>Nibh vel velit auctor aliquet. Aenean sollicitudin, lorem quis bibendum.</p>
  <div class="row"><div class="btn" style="width:77px">Learn More</div><div class="btn" style="width:37px">$ 25</div></div>
</div>
<div class="abs dish" style="left:498px;top:646px">
  <div class="img photo" role="img" aria-label="Homemade burger with lettuce and tomato beside fries" style="background:linear-gradient(160deg,#8a9a5a,#c28a4a 40%,#5a3a22 70%,#d9c7a0)"></div>
  <h3>PROIN GRAVIDA</h3>
  <p>Nibh vel velit auctor aliquet. Aenean sollicitudin, lorem quis bibendum.</p>
  <div class="row"><div class="btn" style="width:77px">Learn More</div><div class="btn" style="width:37px">$ 25</div></div>
</div>
<div class="abs dish" style="left:656px;top:646px">
  <div class="img photo" role="img" aria-label="Sliced steak with salsa and broccoli" style="background:linear-gradient(150deg,#b0a890,#9a3a30 45%,#3e7a22)"></div>
  <h3>PROIN GRAVIDA</h3>
  <p>Nibh vel velit auctor aliquet. Aenean sollicitudin, lorem quis bibendum.</p>
  <div class="row"><div class="btn" style="width:77px">Learn More</div><div class="btn" style="width:37px">$ 25</div></div>
</div>

<div class="abs rule" style="left:183px;top:826px;width:617px"></div>

<!-- About -->
<div class="abs h2" style="left:185px;top:850px">About <em>Us</em></div>
<div class="abs photo" role="img" aria-label="Restaurant interior with wooden chairs and red lighting" style="left:183px;top:883px;width:89px;height:71px;background:linear-gradient(160deg,#6a4a3a,#b2351e 55%,#2a1812)"></div>
<div class="abs body" style="left:289px;top:884px;width:195px">
  <p>This is Photoshop's version &nbsp;of Lorem Ipsum. Proin gravida nibh vel velit auctor aliquet. Aenean sollicitudin, lorem quis bibendum auctor, nisi elit consequat ipsum, nec sagittis sem nibh id elit.</p>
  <p style="margin-top:9px">Duis sed odio sit amet nibh vulputate cursus a sit amet mauris. Morbi accumsan ipsum velit.<br>Nam nec tellus a odio tincidunt auctor a ornare odio.</p>
</div>

<!-- Testimonials -->
<div class="abs h2" style="left:498px;top:850px"><em>Testimonials</em></div>
<div class="abs viewall" style="left:770px;top:839px">VIEW ALL</div>
<div class="abs arrows" style="left:770px;top:853px">
  <span><svg width="5" height="6" viewBox="0 0 5 6"><path d="M4 0L0 3l4 3z" fill="#fff"/></svg></span>
  <span><svg width="5" height="6" viewBox="0 0 5 6"><path d="M1 0l4 3-4 3z" fill="#fff"/></svg></span>
</div>
<div class="abs photo" role="img" aria-label="Customer portrait" style="left:500px;top:883px;width:34px;height:34px;background:linear-gradient(160deg,#d8c0a0,#b89070)"></div>
<div class="abs quote" style="left:551px;top:883px;width:250px">"This is Photoshop's version &nbsp;of Lorem Ipsum. Proin gravida nibh vel velit auctor aliquet. Aenean sollicitudin"<b>Mira Falden</b></div>
<div class="abs photo" role="img" aria-label="Customer portrait" style="left:500px;top:928px;width:34px;height:34px;background:linear-gradient(160deg,#6a5a50,#2a2a30)"></div>
<div class="abs quote" style="left:551px;top:926px;width:250px">"Duis sed odio sit amet nibh vulputate cursus a sit amet mauris. Morbi accumsan ipsum velit.Nam nec tellus a odio tincidunt auctor."<b>Owen Ruest</b></div>

<div class="abs rule" style="left:183px;top:982px;width:616px"></div>
<div class="abs rule" style="left:183px;top:985px;width:616px"></div>

<!-- Book a table -->
<div class="abs h2" style="left:183px;top:1007px">Book a Table</div>
<div class="abs field" style="left:183px;top:1040px;width:143px;height:19px">Full Name</div>
<div class="abs field" style="left:341px;top:1040px;width:142px;height:19px">Book for (Seats)<svg width="6" height="5" viewBox="0 0 6 5"><path d="M0 0h6L3 5z" fill="#666"/></svg></div>
<div class="abs field" style="left:183px;top:1064px;width:143px;height:19px">Contact Number</div>
<div class="abs field" style="left:341px;top:1064px;width:142px;height:19px">Email Address</div>
<div class="abs btn" style="left:183px;top:1089px;width:143px;height:19px">Book a Table Now</div>

<!-- Follow -->
<div class="abs h2" style="left:498px;top:1007px">Follow Us</div>
<p class="abs body" style="left:497px;top:1038px;width:290px">This is Photoshop's version &nbsp;of Lorem Ipsum. Proin gravida nibh vel velit auctor aliquet. Aenean sollicitudin, lorem quis bibendum auctor.</p>
<div class="abs icons" style="left:498px;top:1070px" aria-label="Social links">
  <span style="background:#2f5fa0"></span><span style="background:#2aa4de"></span><span style="background:#e56a1e"></span><span style="background:#c8232c"></span><span style="background:#222"></span><span style="background:#d0302a"></span>
</div>

<footer class="abs footer">
  <a class="active" style="left:184px">Home</a>
  <a style="left:224px">Menu</a>
  <a style="left:263px">Recepies</a>
  <a style="left:316px">Portfolio</a>
  <a style="left:378px">News</a>
  <a style="left:416px">About Us</a>
  <a style="left:471px">Contact Us</a>
  <div class="abs brand-f">OAKBARREL</div>
</footer>
<div class="abs legal">Copyright &nbsp;| &nbsp;All right &nbsp;reserved &nbsp;| &nbsp;Oakbarrel &nbsp;| &nbsp;Privacy Policy</div>
</body>
</html>
```